4 x Designs Required

Hi There,
I require 4 x different designs to be made for 4 new brands of mine however they can be quite interchangeable. HR Plinkr and Marketing Plinkr can be similar just with a difference in colour. The same goes for the Bulletin brands. This means there are ultimately two designs that need perfecting.

There must be a click here CTA on the banner somewhere. :-)

I require the banners in 728x90 format and 960x90 please.

Please use strap lines on the banners such as:
Essential Whitepapers for HR Professionals
Essential Whitepapers for Marketing Professionals
Your No.1 Whitepaper Resource

The brand names:
HR Plinkr
Marketing Plinkr
HR Dispatchly
Marketing Dispatchly

Examples attached.

```html
<!DOCTYPE html>
<html lang="en">
<head>
<meta charset="utf-8">
<title>Plinkr Whitepaper Banners</title>
<link href="https://fonts.googleapis.com/css2?family=Montserrat:ital,wght@0,600;0,700;0,800;1,700;1,800&display=swap" rel="stylesheet">
<style>
  :root {
    --navy: #27235f;
    --navy-deep: #1f2a55;
    --green: #7cc24a;
    --green-light: #8fd05a;
    --yellow: #fbb515;
    --white: #ffffff;
    --sheet-light: #ffffff;
    --sheet-dark: #cfcfcf;
  }
  * { margin: 0; padding: 0; box-sizing: border-box; }
  html, body {
    width: 960px;
    height: 1200px;
    overflow: hidden;
  }
  body {
    position: relative;
    background: radial-gradient(ellipse 70% 45% at 50% 18%, var(--sheet-light) 0%, #ececec 55%, var(--sheet-dark) 100%);
    font-family: "Montserrat", sans-serif;
  }
  .banner {
    position: absolute;
    left: 26px;
    width: 908px;
    height: 113px;
    display: block;
    box-shadow: 0 1px 3px rgba(0,0,0,0.15);
  }
  .banner--one   { top: 133px; }
  .banner--two   { top: 373px; }
  .banner--three { top: 613px; }
  .banner--four  { top: 853px; }

  .badge-text { font-family: "Montserrat", sans-serif; font-weight: 700; text-anchor: middle; }
  .badge-text .badge-no { font-weight: 800; }
  .brand-name { font-family: "Montserrat", sans-serif; font-weight: 800; }
  .strapline { font-family: "Montserrat", sans-serif; font-weight: 800; font-style: italic; }
  .headline { font-family: "Montserrat", sans-serif; font-weight: 800; }
  .cta-label { font-family: "Montserrat", sans-serif; font-weight: 800; text-anchor: middle; }
</style>
</head>
<body>

<!-- Marketing banner -->
<svg class="banner banner--one" viewBox="0 0 908 113" xmlns="http://www.w3.org/2000/svg" aria-label="Marketing Plinkr banner">
  <defs>
    <linearGradient id="mk-photo-a" x1="0" x2="1" y1="0" y2="0">
      <stop offset="0" stop-color="#e9ebf1"/>
      <stop offset="0.55" stop-color="#d6d9e2"/>
      <stop offset="1" stop-color="#7cc24a"/>
    </linearGradient>
    <linearGradient id="mk-green-a" x1="0" x2="0" y1="0" y2="1">
      <stop offset="0" stop-color="#86c956"/>
      <stop offset="1" stop-color="#6db43f"/>
    </linearGradient>
  </defs>
  <rect width="908" height="113" fill="url(#mk-green-a)"/>
  <rect class="banner-photo" role="img" aria-label="Laptop showing an analytics dashboard" x="0" y="0" width="300" height="113" fill="url(#mk-photo-a)"/>
  <polygon class="badge" points="262,17 376,17 400,62 376,107 262,107 238,62" fill="var(--navy-deep)"/>
  <text class="badge-text" fill="var(--green-light)" x="319" y="0">
    <tspan x="319" y="49" font-size="16">Your <tspan class="badge-no" font-size="25">No.1</tspan></tspan>
    <tspan x="319" y="71" font-size="15">Whitepaper</tspan>
    <tspan x="319" y="92" font-size="15">Resource</tspan>
  </text>
  <text class="brand-name" fill="var(--navy-deep)" x="876" y="30" font-size="25" text-anchor="end">Marketing Plinkr</text>
  <text class="strapline" fill="var(--navy-deep)" font-size="17">
    <tspan x="410" y="54">“Essential Whitepapers for</tspan>
    <tspan x="724" y="76" text-anchor="end">Marketing Professionals...”</tspan>
  </text>
  <g class="cta">
    <polygon points="750,68 880,68 880,100 748,100 744,82" fill="var(--navy-deep)"/>
    <text class="cta-label" fill="var(--white)" x="814" y="91" font-size="17">CLICK HERE</text>
  </g>
  <rect width="908" height="113" fill="none" stroke="var(--navy-deep)" stroke-width="2"/>
</svg>

<!-- HR banner -->
<svg class="banner banner--two" viewBox="0 0 908 113" xmlns="http://www.w3.org/2000/svg" aria-label="HR Plinkr banner">
  <defs>
    <linearGradient id="hr-photo-a" x1="0" x2="1" y1="0" y2="0">
      <stop offset="0" stop-color="#cfd3e2"/>
      <stop offset="0.6" stop-color="#9ea5ba"/>
      <stop offset="1" stop-color="#545c70"/>
    </linearGradient>
  </defs>
  <rect width="908" height="113" fill="var(--navy)"/>
  <rect class="banner-photo" role="img" aria-label="Laptop on a desk showing charts" x="600" y="0" width="308" height="113" fill="url(#hr-photo-a)"/>
  <path d="M600 0 Q628 40 640 113 H600 Z" fill="var(--navy)"/>
  <path d="M0 0 H60 Q22 42 12 113 H0 Z" fill="var(--yellow)"/>
  <text class="headline" fill="var(--yellow)" x="76" y="41" font-size="20">Essential Whitepapers for HR Professionals...</text>
  <text class="brand-name" fill="var(--yellow)" x="76" y="89" font-size="24">HR Plinkr</text>
  <g class="cta">
    <rect x="376" y="67" width="110" height="28" rx="14" fill="var(--yellow)"/>
    <text class="cta-label" fill="var(--navy)" x="431" y="86" font-size="14">Click Here</text>
  </g>
  <polygon class="badge" points="590,10 690,6 706,50 696,110 606,112 556,96 566,48" fill="var(--yellow)"/>
  <text class="badge-text" fill="var(--navy)">
    <tspan x="633" y="59" font-size="16">Your <tspan class="badge-no" font-size="25">No.1</tspan></tspan>
    <tspan x="633" y="78" font-size="15">Whitepaper</tspan>
    <tspan x="633" y="97" font-size="15">Resource</tspan>
  </text>
  <rect width="908" height="113" fill="none" stroke="var(--navy)" stroke-width="2"/>
</svg>

<!-- Marketing banner, second size -->
<svg class="banner banner--three" viewBox="0 0 908 113" xmlns="http://www.w3.org/2000/svg" aria-label="Marketing Plinkr banner">
  <defs>
    <linearGradient id="mk-photo-b" x1="0" x2="1" y1="0" y2="0">
      <stop offset="0" stop-color="#e9ebf1"/>
      <stop offset="0.55" stop-color="#d6d9e2"/>
      <stop offset="1" stop-color="#7cc24a"/>
    </linearGradient>
    <linearGradient id="mk-green-b" x1="0" x2="0" y1="0" y2="1">
      <stop offset="0" stop-color="#86c956"/>
      <stop offset="1" stop-color="#6db43f"/>
    </linearGradient>
  </defs>
  <rect width="908" height="113" fill="url(#mk-green-b)"/>
  <rect class="banner-photo" role="img" aria-label="Laptop showing an analytics dashboard" x="0" y="0" width="300" height="113" fill="url(#mk-photo-b)"/>
  <polygon class="badge" points="262,17 376,17 400,62 376,107 262,107 238,62" fill="var(--navy-deep)"/>
  <text class="badge-text" fill="var(--green-light)">
    <tspan x="319" y="49" font-size="16">Your <tspan class="badge-no" font-size="25">No.1</tspan></tspan>
    <tspan x="319" y="71" font-size="15">Whitepaper</tspan>
    <tspan x="319" y="92" font-size="15">Resource</tspan>
  </text>
  <text class="brand-name" fill="var(--navy-deep)" x="876" y="30" font-size="25" text-anchor="end">Marketing Plinkr</text>
  <text class="strapline" fill="var(--navy-deep)" font-size="17">
    <tspan x="410" y="54">“Essential Whitepapers for</tspan>
    <tspan x="724" y="76" text-anchor="end">Marketing Professionals...”</tspan>
  </text>
  <g class="cta">
    <polygon points="750,68 880,68 880,100 748,100 744,82" fill="var(--navy-deep)"/>
    <text class="cta-label" fill="var(--white)" x="814" y="91" font-size="17">CLICK HERE</text>
  </g>
</svg>

<!-- HR banner, second size -->
<svg class="banner banner--four" viewBox="0 0 908 113" xmlns="http://www.w3.org/2000/svg" aria-label="HR Plinkr banner">
  <defs>
    <linearGradient id="hr-photo-b" x1="0" x2="1" y1="0" y2="0">
      <stop offset="0" stop-color="#cfd3e2"/>
      <stop offset="0.6" stop-color="#9ea5ba"/>
      <stop offset="1" stop-color="#545c70"/>
    </linearGradient>
  </defs>
  <rect width="908" height="113" fill="var(--navy)"/>
  <rect class="banner-photo" role="img" aria-label="Laptop on a desk showing charts" x="600" y="0" width="308" height="113" fill="url(#hr-photo-b)"/>
  <path d="M600 0 Q628 40 640 113 H600 Z" fill="var(--navy)"/>
  <path d="M0 0 H60 Q22 42 12 113 H0 Z" fill="var(--yellow)"/>
  <text class="headline" fill="var(--yellow)" x="76" y="41" font-size="20">Essential Whitepapers for HR Professionals...</text>
  <text class="brand-name" fill="var(--yellow)" x="76" y="89" font-size="24">HR Plinkr</text>
  <g class="cta">
    <rect x="376" y="67" width="110" height="28" rx="14" fill="var(--yellow)"/>
    <text class="cta-label" fill="var(--navy)" x="431" y="86" font-size="14">Click Here</text>
  </g>
  <polygon class="badge" points="590,10 690,6 706,50 696,110 606,112 556,96 566,48" fill="var(--yellow)"/>
  <text class="badge-text" fill="var(--navy)">
    <tspan x="633" y="59" font-size="16">Your <tspan class="badge-no" font-size="25">No.1</tspan></tspan>
    <tspan x="633" y="78" font-size="15">Whitepaper</tspan>
    <tspan x="633" y="97" font-size="15">Resource</tspan>
  </text>
</svg>

</body>
</html>
```